creation of a business card design for a company specializing in the creation...

I would like to create a design for a professional business card on a black background and with the company's colors (I am attaching some files: including the logo in horizontal and centered format, I am also attaching a recent project design a T-shirt, this is the one I chose to give you an idea of my preferences.

we are in the process of developing a new website design, it is still in the development phase but it can be viewed at the following address: www.vendrelak.be to give you other ideas about the company
you will see for yourself the subject of my main activity: company specializing in the construction of stairs

I would like a business card that stands out from the rest with a unique design

here is the informations
Name: Florent Dubrec
Function: Manager
Address: Rue Masquelin du Pont 41
7180 La Louvière
telephone: +32 486 219 508
email: info@rv8k.be
website: rv8k. be
social networks: Facebook, YouTube, TikTok, Instagram

Target Market(s)

customer who wants to have a beautiful staircase built

Industry/Entity Type

contruction d'escalier

Contact Information for Business Card

Adresse. Numero de telephone, site web, le texte : "Createur d'escalier", logo recto-verso, icone des reseaux sociaux

Requirements
Must have
• the mention: Stair creator
Nice to have
• an illustration of a designer staircase
Should not have
• do not distort the logo

```html
<!DOCTYPE html>
<html lang="en">
<head>
<meta charset="utf-8">
<title>RV8K business card</title>
<link rel="stylesheet" href="https://fonts.googleapis.com/css2?family=Montserrat:wght@300;400;500;600&display=swap">
<style>
  :root {
    --backdrop: #2b2b2e;
    --card: #161618;
    --card-edge: #202023;
    --emboss: #2c2c30;
    --emboss-light: #3a3a3f;
    --accent: #6e9fc4;
    --ink: #f2f2f2;
    --ink-soft: #cfcfd2;
  }
  * { margin: 0; padding: 0; box-sizing: border-box; }
  html, body { width: 1200px; height: 900px; overflow: hidden; }
  body {
    background: var(--backdrop);
    font-family: "Montserrat", sans-serif;
    display: flex;
    align-items: center;
    justify-content: center;
    gap: 40px;
  }
  .card {
    position: relative;
    width: 540px;
    height: 310px;
    background: var(--card);
    border: 1px solid var(--card-edge);
    border-radius: 16px;
    overflow: hidden;
  }

  /* Front */
  .front { display: flex; align-items: center; justify-content: center; gap: 22px; }
  .front .brand-mark { width: 56px; height: 56px; background: var(--emboss); }
  .front .brand-text { display: flex; flex-direction: column; align-items: flex-end; }
  .front .brand-name {
    font-weight: 400; font-size: 86px; line-height: 86px;
    letter-spacing: 6px; color: var(--emboss-light);
  }
  .front .tagline {
    font-size: 11px; letter-spacing: 5px; text-transform: uppercase;
    color: var(--emboss-light); margin-top: 6px;
  }

  /* Back */
  .brand {
    position: absolute; left: 40px; top: 40px;
    display: flex; align-items: center; gap: 14px;
  }
  .brand-square { width: 40px; height: 40px; background: var(--accent); }
  .brand .brand-text { display: flex; flex-direction: column; }
  .brand .brand-name {
    font-weight: 400; font-size: 44px; line-height: 46px; letter-spacing: 4px; color: var(--ink);
  }
  .brand .tagline {
    font-size: 8px; letter-spacing: 3.4px; text-transform: uppercase;
    color: var(--ink-soft); margin-top: 2px;
  }
  .divider { position: absolute; left: 0; top: 0; width: 540px; height: 310px; }
  .divider line { stroke: var(--accent); stroke-width: 2; }
  .person { position: absolute; left: 342px; top: 126px; }
  .person-name { font-weight: 600; font-size: 21px; color: var(--accent); }
  .person-role { font-weight: 400; font-size: 12px; color: var(--ink-soft); margin-top: 2px; }
  .address {
    position: absolute; left: 40px; top: 188px;
    font-size: 13px; line-height: 18px; color: var(--ink);
  }
  .contacts {
    position: absolute; left: 40px; top: 236px;
    list-style: none; font-size: 13px; color: var(--ink);
  }
  .contacts li { display: flex; align-items: center; gap: 12px; height: 21px; }
  .contacts svg { width: 12px; height: 12px; fill: var(--accent); }
  .socials {
    position: absolute; right: 36px; top: 232px;
    display: flex; gap: 9px;
  }
  .socials span { width: 14px; height: 14px; border-radius: 3px; background: var(--accent); }
</style>
</head>
<body>
  <section class="card front" aria-label="Card front">
    <span class="brand-mark"></span>
    <div class="brand-text">
      <span class="brand-name">RV8K</span>
      <span class="tagline">Stair creator</span>
    </div>
  </section>

  <section class="card back" aria-label="Card back">
    <div class="brand">
      <span class="brand-square"></span>
      <div class="brand-text">
        <span class="brand-name">RV8K</span>
        <span class="tagline">Stair creator</span>
      </div>
    </div>
    <svg class="divider" viewBox="0 0 540 310" aria-hidden="true">
      <line x1="30" y1="180" x2="334" y2="152"/>
    </svg>
    <div class="person">
      <p class="person-name">Florent Dubrec</p>
      <p class="person-role">Manager</p>
    </div>
    <p class="address">Rue Masquelin du Pont 41<br>7180 La Louvière</p>
    <ul class="contacts">
      <li>
        <svg viewBox="0 0 24 24" aria-hidden="true"><path d="M6.6 10.8a15 15 0 0 0 6.6 6.6l2.2-2.2a1 1 0 0 1 1-.25 11.4 11.4 0 0 0 3.6.57 1 1 0 0 1 1 1V20a1 1 0 0 1-1 1A17 17 0 0 1 3 4a1 1 0 0 1 1-1h3.5a1 1 0 0 1 1 1c0 1.25.2 2.45.57 3.57a1 1 0 0 1-.25 1z"/></svg>
        +32 486 219 508
      </li>
      <li>
        <svg viewBox="0 0 24 24" aria-hidden="true"><path d="M2 5h20v14H2z M2 5l10 8 10-8"/></svg>
        info@rv8k.be
      </li>
      <li>
        <svg viewBox="0 0 24 24" aria-hidden="true"><circle cx="12" cy="12" r="10"/></svg>
        www.rv8k.be
      </li>
    </ul>
    <div class="socials" aria-label="Social networks">
      <span></span><span></span><span></span><span></span>
    </div>
  </section>
</body>
</html>
```